Concierge Healthcare Business Card Design and Logo

We need a logo and business card design for a new company called "Sound Harbor". We will provide concierge audiological care, hearing aids, hearing exams, custom hearing protection etc to patients in the comfort of their homes and offices. We would like a sleek and modern design preferably with an Ear related logo.

Target Market(s)

People with hearing loss, Hunters, Musicians
My usual clientele are older individuals so usually 50+ years old

Industry/Entity Type

Health Care

Contact Information for Business Card

Delia Franks, AuD
Audiologist
512-648-2917
soundharbor@mailnest.com
www.soundharbor-example.com

Logo Text

Sound Harbor

Number of Pages Required

3 page

```html
<!DOCTYPE html>
<html lang="en">
<head>
<meta charset="utf-8">
<title>Sound Harbor – Business Cards</title>
<link rel="stylesheet" href="https://fonts.googleapis.com/css2?family=Arimo:wght@400;700&display=swap">
<style>
  :root {
    --teal: #2bbcc2;
    --orange: #f4b234;
    --card: #ffffff;
    --card-edge: #e3e5e6;
    --backdrop: #e9eaeb;
    --text-soft: #8a8f92;
  }
  * { box-sizing: border-box; margin: 0; padding: 0; }
  html, body { width: 1200px; height: 1023px; overflow: hidden; }
  body {
    background: var(--backdrop);
    font-family: "Arimo", Arial, sans-serif;
    position: relative;
  }
  .card {
    position: absolute;
    width: 560px;
    height: 320px;
    background: linear-gradient(135deg, #ffffff 0%, #f6f7f7 100%);
    border: 1px solid var(--card-edge);
    border-radius: 12px;
    box-shadow: 0 6px 18px rgba(0,0,0,0.12);
  }
  .card--front { left: 80px; top: 120px; }
  .card--back { left: 560px; top: 580px; }

  .brand {
    display: flex;
    align-items: center;
    gap: 14px;
    font-weight: 700;
    color: var(--teal);
    white-space: nowrap;
  }
  .brand__dot {
    border-radius: 50%;
    background: var(--teal);
    flex: none;
  }
  .card--front .brand {
    position: absolute;
    left: 50%; top: 50%;
    transform: translate(-50%, -50%);
    font-size: 54px;
  }
  .card--front .brand__dot { width: 48px; height: 48px; }

  .card--back .brand {
    position: absolute;
    left: 38px; top: 40px;
    font-size: 34px;
  }
  .card--back .brand__dot { width: 32px; height: 32px; }

  .divider {
    position: absolute;
    left: 190px; top: 126px;
    width: 340px; height: 2px;
    background: linear-gradient(90deg, rgba(43,188,194,0) 0%, var(--teal) 40%, rgba(43,188,194,0.2) 100%);
  }
  .contact {
    position: absolute;
    left: 250px; top: 148px;
  }
  .contact__name {
    color: var(--teal);
    font-size: 22px;
    font-weight: 700;
    letter-spacing: -0.3px;
  }
  .contact__cred { font-size: 13px; font-weight: 400; }
  .contact__role {
    color: var(--orange);
    font-size: 13px;
    margin-top: 3px;
    margin-bottom: 14px;
  }
  .contact__list { list-style: none; }
  .contact__item {
    display: flex;
    align-items: center;
    gap: 10px;
    color: var(--orange);
    font-size: 14px;
    line-height: 24px;
  }
  .contact__icon { width: 14px; height: 14px; flex: none; }
</style>
</head>
<body>
  <section class="card card--front" aria-label="Business card front">
    <div class="brand"><span class="brand__dot"></span>Sound Harbor</div>
  </section>

  <section class="card card--back" aria-label="Business card back">
    <div class="brand"><span class="brand__dot"></span>Sound Harbor</div>
    <div class="divider"></div>
    <div class="contact">
      <p class="contact__name">Delia Franks<span class="contact__cred">, AuD</span></p>
      <p class="contact__role">Audiologist</p>
      <ul class="contact__list">
        <li class="contact__item">
          <svg class="contact__icon" viewBox="0 0 16 16" aria-hidden="true">
            <circle cx="8" cy="8" r="7" fill="none" stroke="#2bbcc2" stroke-width="1.4"/>
            <path d="M5.5 4.5l1.5 0 .7 2-1 .8a5 5 0 0 0 2 2l.8-1 2 .7v1.5c-3 .5-6.5-3-6-6z" fill="#2bbcc2"/>
          </svg>
          512-648-2917
        </li>
        <li class="contact__item">
          <svg class="contact__icon" viewBox="0 0 16 16" aria-hidden="true">
            <rect x="1" y="3" width="14" height="10" rx="1" fill="#2bbcc2"/>
            <path d="M1.5 3.5L8 9l6.5-5.5" fill="none" stroke="#fff" stroke-width="1.3"/>
          </svg>
          soundharbor@mailnest.com
        </li>
        <li class="contact__item">
          <svg class="contact__icon" viewBox="0 0 16 16" aria-hidden="true">
            <circle cx="8" cy="8" r="6.5" fill="none" stroke="#2bbcc2" stroke-width="1.3"/>
            <ellipse cx="8" cy="8" rx="3" ry="6.5" fill="none" stroke="#2bbcc2" stroke-width="1.1"/>
            <path d="M1.5 8h13M2.5 5h11M2.5 11h11" stroke="#2bbcc2" stroke-width="1"/>
          </svg>
          www.soundharbor-example.com
        </li>
      </ul>
    </div>
  </section>
</body>
</html>
```